Advertisements needed for new pub to expand clientele

I need a few different advert. done for my business, can use the same background for all, that covers the following

- New Late Night Menu with Back To School Late Night Prices Thursday-Saturday while bar is open

- $25 gift card to be drawn on September 30th with Liking our facebook page, sharing the ad., and using the hashtag #StirTheSkillet

- Happy Hour Pints $7 & Buy 3 Pints get a free Pretzel Bites between 4:00-5:00 PM

http://www.pinecovetaphouse.com/

https://www.facebook.com/PnCovePub/

Target Market(s)

Restaurant Diners

Industry/Entity Type

Business

Requirements
Must have
• Logo of Pub
• Key information in description for each

```html
<!DOCTYPE html>
<html lang="en">
<head>
<meta charset="utf-8">
<title>Pine Cove Pub – Late Night Menu</title>
<link href="https://fonts.googleapis.com/css2?family=Montserrat:wght@300;400;500;700;800&display=swap" rel="stylesheet">
<style>
  :root {
    --ink: #1c1c1c;
    --card: rgba(255, 255, 255, 0.72);
    --night: #000000;
    --paper: #ffffff;
    --muted: #d6d6d6;
    --photo-warm: #e8a35a;
    --photo-cream: #f2e6d4;
    --photo-green: #6f8f4a;
  }
  * { box-sizing: border-box; margin: 0; padding: 0; }
  html, body { width: 1200px; height: 850px; overflow: hidden; background: var(--paper); }
  body { font-family: "Montserrat", sans-serif; color: var(--ink); }

  .flyer { position: relative; width: 1200px; height: 850px; overflow: hidden; }

  /* Menu side */
  .menu-side { position: absolute; left: 0; top: 0; width: 600px; height: 850px; }
  .food-photo {
    position: absolute; inset: 0;
    background:
      radial-gradient(ellipse 260px 200px at 300px 420px, var(--photo-warm), transparent 70%),
      radial-gradient(ellipse 120px 260px at 20px 500px, var(--photo-green), transparent 70%),
      radial-gradient(ellipse 300px 200px at 420px 700px, #f0c48a, transparent 70%),
      linear-gradient(160deg, var(--photo-cream), #e9cfa8 55%, #d9a86a);
  }
  .menu-card { position: absolute; left: 0; top: 0; }

  .menu-title {
    position: absolute; left: 0; width: 600px; top: 66px;
    text-align: center; font-weight: 800; font-size: 58px; line-height: 60px;
    letter-spacing: 5px; color: var(--ink);
  }
  .rule { position: absolute; left: 72px; width: 454px; height: 5px; background: var(--ink); }
  .rule.top { top: 209px; }
  .rule.mid { top: 258px; height: 4px; }
  .rule.bottom { top: 727px; left: 74px; width: 452px; }
  .promo-line {
    position: absolute; left: 0; width: 600px; top: 222px;
    text-align: center; font-weight: 700; font-size: 22px;
  }
  .column-divider { position: absolute; left: 300px; top: 296px; width: 2px; height: 430px; background: var(--ink); }

  .menu-item {
    position: absolute; font-size: 18.5px; line-height: 23px; font-weight: 400;
    display: flex; justify-content: space-between; align-items: center;
  }
  .menu-item.left { left: 73px; width: 218px; }
  .menu-item.right { left: 308px; width: 216px; }
  .price { font-size: 19px; font-weight: 500; white-space: nowrap; }
  .price.raised { align-self: flex-start; }
  .price sup { font-size: 11px; vertical-align: 7px; }

  .menu-note {
    position: absolute; left: 0; width: 600px; top: 740px;
    text-align: center; font-size: 20px; font-weight: 400;
  }

  /* Info side */
  .info-side { position: absolute; left: 600px; top: 0; width: 600px; height: 850px; background: var(--night); color: var(--paper); }
  .pub-mark {
    position: absolute; left: 195px; top: 95px; width: 210px; height: 210px;
    border: 3px solid var(--paper); border-radius: 50%;
    display: flex; align-items: center; justify-content: center; text-align: center;
    font-size: 30px; font-weight: 500; line-height: 36px; letter-spacing: 1px;
  }
  .tagline {
    position: absolute; left: 0; width: 600px; top: 340px; text-align: center;
    font-size: 19.5px; font-weight: 300; letter-spacing: 1.5px; color: var(--muted);
  }
  .info-rule { position: absolute; left: 98px; width: 404px; height: 5px; background: var(--paper); }
  .info-rule.upper { top: 412px; }
  .info-rule.lower { top: 543px; }
  .contact { position: absolute; left: 195px; top: 438px; font-size: 20px; line-height: 26px; font-weight: 400; }
  .hours-label { position: absolute; left: 227px; font-size: 17px; font-weight: 400; letter-spacing: 0.5px; }
  .hours-lines { position: absolute; left: 227px; font-size: 17px; line-height: 23px; }
  .hours-icon { position: absolute; }
</style>
</head>
<body>
<main class="flyer">
  <section class="menu-side">
    <div class="food-photo" role="img" aria-label="Close-up photo of seared scallops with pork belly and greens on a plate"></div>
    <svg class="menu-card" width="600" height="850" viewBox="0 0 600 850" aria-hidden="true">
      <path d="M44 40 H558 A14 14 0 0 0 572 54 V798 A14 14 0 0 0 558 812 H44 A14 14 0 0 0 30 798 V54 A14 14 0 0 0 44 40 Z" fill="rgba(255,255,255,0.72)"/>
    </svg>

    <h1 class="menu-title">LATE<br>NIGHT</h1>
    <div class="rule top"></div>
    <p class="promo-line">Back To School Late Night Prices</p>
    <div class="rule mid"></div>
    <div class="column-divider"></div>

    <div class="menu-item left" style="top:298px"><span>Buffalo Braised<br>Chicken Taco Duo</span><span class="price"><sup>$</sup>13</span></div>
    <div class="menu-item left" style="top:371px"><span>Mole Braised Beef<br>Taco Duo</span><span class="price"><sup>$</sup>14</span></div>
    <div class="menu-item left" style="top:439px"><span>Confit Duck<br>Wings</span><span class="price"><sup>$</sup>14</span></div>
    <div class="menu-item left" style="top:510px"><span>Scallops and<br>Pork Belly</span><span class="price"><sup>$</sup>16</span></div>
    <div class="menu-item left" style="top:580px"><span>Smoked Meat<br>Reuben</span><span class="price"><sup>$</sup>21</span></div>
    <div class="menu-item left" style="top:647px"><span>The Cove "Mac"</span><span class="price"><sup>$</sup>22</span></div>
    <div class="menu-item left" style="top:694px"><span>The Burger</span><span class="price"><sup>$</sup>22</span></div>

    <div class="menu-item right" style="top:298px"><span>The Poutine</span><span class="price raised"><sup>$</sup>14</span></div>
    <div class="menu-item right" style="top:371px"><span>"It Tastes<br>Like Chicken"</span><span class="price"><sup>$</sup>13</span></div>
    <div class="menu-item right" style="top:439px"><span>Smolked Atlantic<br>Salmon</span><span class="price"><sup>$</sup>22</span></div>
    <div class="menu-item right" style="top:510px"><span>Smolked Atlantic<br>Salmon</span><span class="price"><sup>$</sup>13</span></div>
    <div class="menu-item right" style="top:578px"><span>Buffalo Fried<br>Veggies</span><span class="price"><sup>$</sup>12</span></div>
    <div class="menu-item right" style="top:647px"><span>Fish N' Grits</span><span class="price"><sup>$</sup>25</span></div>
    <div class="menu-item right" style="top:692px"><span>Pretzel Bites</span><span class="price"><sup>$</sup>25</span></div>

    <div class="rule bottom"></div>
    <p class="menu-note">Thursday-Saturday while bar is open</p>
  </section>

  <section class="info-side">
    <div class="pub-mark">Pine Cove<br>Pub</div>
    <p class="tagline">LOCALLY SOURCED × CRAFTED WITH LOVE</p>
    <div class="info-rule upper"></div>
    <address class="contact" style="font-style:normal">
      14 Harbour Lane<br>
      Northport, NL A1C4K7<br>
      <svg width="16" height="16" viewBox="0 0 16 16" aria-hidden="true" style="vertical-align:-2px"><circle cx="8" cy="8" r="7" fill="none" stroke="#fff" stroke-width="1.2"/><path d="M5.5 4.5 l1.5 1.5 -1 1 q1 2 3 3 l1-1 1.5 1.5 -1.2 1.2 q-4-1-6-6 z" fill="#fff"/></svg> (709) 555-0182
    </address>
    <div class="info-rule lower"></div>

    <p class="hours-label" style="top:610px">FOOD HOURS</p>
    <svg class="hours-icon" style="left:174px;top:646px" width="38" height="40" viewBox="0 0 38 40" aria-hidden="true">
      <path d="M4 36 L32 6" stroke="#fff" stroke-width="3" stroke-linecap="round"/>
      <path d="M34 36 L8 8 M4 4 L12 12 M8 2 L14 8 M2 8 L8 14" stroke="#fff" stroke-width="2.5" stroke-linecap="round"/>
    </svg>
    <p class="hours-lines" style="top:643px">Tu-Th 11:30-2 &amp; 5-9:30<br>F-Sa&nbsp; 11:30-3 &amp; 4-10</p>

    <p class="hours-label" style="top:713px">BAR HOURS</p>
    <svg class="hours-icon" style="left:174px;top:740px" width="36" height="48" viewBox="0 0 36 48" aria-hidden="true">
      <path d="M18 4 q5 2 0 5 q-5 3 0 6 q5 3 0 6 V34" fill="none" stroke="#fff" stroke-width="2.2"/>
      <rect x="3" y="34" width="30" height="6" rx="3" fill="none" stroke="#fff" stroke-width="2.2"/>
      <circle cx="6" cy="37" r="4" fill="none" stroke="#fff" stroke-width="2"/>
      <circle cx="30" cy="37" r="4" fill="none" stroke="#fff" stroke-width="2"/>
    </svg>
    <p class="hours-lines" style="top:746px">Tu-Th 4-11<br>F-Sa&nbsp; 4–1</p>
  </section>
</main>
</body>
</html>
```